A Brochure to sell LED Downlights to clients

I am starting a campaign on zestoria for LED down lights the link to the landing page can be found at brindlemoss.com.au/led .

When the client send a contact request i want to be able to send back a brochure of a picture of each light (Approx 6 - 8 types) and have a few sentences on each light and price brake down.

'Quarnil Sabeto 9w LED'

**Information**

1-10 lights $49
11-20 lights $45
21 - 40 lights $42
40 and over $40

EACH LIGHT:

Hi,

This is very good.

I
But,

Each light will have its own price.

Can i get it made like this;

Picture - Spec - Pricing in a table style please? - i like the layout it just need to suit the tables under:

picture - Brand - Price 1-10
Model - Price 11-20
Watts - Price 21-21
lumen - price 30- 40
Warranty = price 40+

Model - Price 11-20
Watts - Price 21-21
lumen - price 30- 40
Warranty = price 40+

Model - Price 11-20
Watts - Price 21-21
lumen - price 30- 40
Warranty = price 40+

and so on....

I want it to be on Microsoft Word so i can easily chop and edit the prices and images also. (So i can print to PDF)

For more information see my website to seek inspiration. I have a zip file of my logo for actual creation and should be also to source pictures of the lights when finalising the design.

brindlemoss.com.au

Thanks

Target Market(s)

Homeowners/commercial business owners

Industry/Entity Type

Electric Company

Font styles to use
Sans Serif

Colors
86cfc6
ffffff
000000

Requirements
Must have
• Professional looking, Colours to the theme of my logo/website
Nice to have
• An awesome design that sells it's self!!!!!!!
• My Logo font is 'Radikil" it would be nice to follow that theme if it doesn't look good i am open to have a nice legible font for the copy.
Should not have
• Cheesy light globes or images

```html
<!DOCTYPE html>
<html lang="en">
<head>
<meta charset="utf-8">
<title>Brindlemoss Electrical – LED Downlights Catalog</title>
<link rel="stylesheet" href="https://fonts.googleapis.com/css2?family=Fredoka:wght@500;600&family=Questrial&display=swap">
<style>
  :root{
    --stage:#232323;
    --teal:#12a89b;
    --teal-deep:#0a9d90;
    --teal-light:#86cfc6;
    --paper:#f7f7f6;
    --ink:#3c3c3c;
    --slate:#4a4a4a;
    --panel-dark:#3f4040;
    --white:#ffffff;
  }
  *{box-sizing:border-box;margin:0;padding:0}
  html,body{width:1200px;height:2980px;overflow:hidden;background:var(--stage)}
  body{position:relative;font-family:"Questrial",sans-serif;color:var(--ink)}
  .page{position:absolute;overflow:hidden;box-shadow:0 4px 14px rgba(0,0,0,.45)}

  /* Cover */
  .cover{left:290px;top:95px;width:622px;height:880px;background:var(--paper)}
  .cover-backdrop{position:absolute;inset:0;background:linear-gradient(180deg,#f2f1ef 0%,#ecebe8 45%,#f5f4f2 70%,#fafafa 100%)}
  .cover-title{position:absolute;right:32px;top:118px;text-align:right;line-height:1}
  .cover-title .word{display:block;font-size:46px;color:var(--teal);letter-spacing:1px}
  .cover-title .years{display:block;font-size:44px;color:var(--slate);margin-top:2px}
  .tile{position:absolute}
  .tile.slate{left:134px;top:254px;width:178px;height:174px;background:#4d4d4d}
  .tile.kitchen-wide{left:318px;top:254px;width:304px;height:174px;background:linear-gradient(135deg,#5a3a24,#a77a4d 55%,#e0c9a4)}
  .tile.boardroom{left:0;top:432px;width:128px;height:174px;background:linear-gradient(160deg,#2b2119,#8c6a3d 60%,#d8b67c)}
  .tile.kitchen-small{left:132px;top:432px;width:178px;height:174px;background:linear-gradient(150deg,#6d4a2f,#b88c5e 60%,#e6d3b5)}
  .tile.brand{left:318px;top:432px;width:178px;height:174px;background:var(--teal);display:flex;flex-direction:column;align-items:center;justify-content:center;color:var(--white)}
  .brand-name{font-family:"Questrial",sans-serif;font-size:25px;color:var(--white);line-height:1.05;text-align:center}
  .brand-name small{display:block;font-size:25px}
  .brand-mark{width:14px;height:14px;background:var(--white);margin-bottom:10px}
  .cover-url{position:absolute;left:0;right:0;top:812px;text-align:center;font-size:22px;letter-spacing:1.5px;color:var(--slate)}

  /* Price page */
  .pricing{left:278px;top:1061px;width:642px;height:902px;background:linear-gradient(180deg,#ececec,#f6f6f6 40%,#eeeeee)}
  .pricing-title{position:absolute;left:0;right:0;top:14px;text-align:center;font-family:"Fredoka",sans-serif;font-weight:600;font-size:38px;line-height:48px;color:var(--teal);letter-spacing:.5px}
  .product-table{position:absolute;left:24px;top:138px;width:596px;height:564px;border:3px solid var(--teal);border-radius:18px;background:var(--white);overflow:hidden}
  .table-head{display:flex;height:36px;background:var(--teal);color:var(--white);font-size:17px}
  .table-head span{display:flex;align-items:center;justify-content:center}
  .col-photo{width:158px}
  .col-spec{width:296px}
  .col-price{flex:1}
  .table-row{display:flex;height:131px;border-top:3px solid var(--teal)}
  .table-head + .table-row{border-top:none}
  .table-row .col-photo{display:flex;align-items:center;justify-content:center;border-right:3px solid var(--teal)}
  .light-photo{width:90px;height:90px;border-radius:50%}
  .light-photo.white{background:radial-gradient(circle,#ffffff 30%,#d9d9d9 75%,#bdbdbd)}
  .light-photo.black{background:radial-gradient(circle,#4a4a4a 25%,#1d1d1d 70%,#f0f0f0 71%)}
  .light-photo.silver{background:radial-gradient(circle,#cfcfcf 30%,#8f8f8f 65%,#6c7a4a 80%,#f0f0f0 81%)}
  .table-row .col-spec{padding:10px 14px;border-right:3px solid var(--teal)}
  .spec-name{font-size:18px;color:var(--teal);margin-bottom:6px}
  .spec-list{list-style:none}
  .spec-list li{display:flex;align-items:center;font-size:12.5px;line-height:19px;color:#333}
  .spec-list li::before{content:"";width:10px;height:10px;border-radius:50%;background:var(--teal);margin-right:9px;flex:none}
  .table-row .col-price{display:flex;align-items:center;justify-content:center;font-family:"Fredoka",sans-serif;font-weight:600;font-size:29px;color:var(--teal)}
  .bulk-tab{position:absolute;left:192px;top:724px;width:260px;height:30px;background:var(--teal);color:var(--white);font-size:17px;display:flex;align-items:center;justify-content:center;z-index:2}
  .bulk-panel{position:absolute;left:26px;top:740px;width:596px;height:122px;border:3px solid var(--teal);border-radius:20px;background:var(--panel-dark);color:var(--white);display:grid;grid-template-columns:1fr 1fr;align-content:center;row-gap:4px;padding:20px 36px 0}
  .bulk-panel p{font-size:20px}
  .bulk-panel p:nth-child(even){padding-left:90px}
  .bulk-panel b{font-weight:400;color:var(--teal)}
  .pricing-url{position:absolute;right:22px;top:868px;font-size:15px;color:var(--slate)}

  /* Back cover */
  .back{left:290px;top:2025px;width:622px;height:878px;background:var(--teal)}
  .back-strip{position:absolute;left:0;top:0;width:100%;height:14px;background:#6d6d6d}
  .back-scene{position:absolute;left:0;top:14px;width:100%;height:864px;background:linear-gradient(180deg,#0a9e91 0%,#17aa9d 35%,#0f9a8d 60%,#13a699 100%)}
  .back-brand{position:absolute;left:0;right:0;top:280px;display:flex;flex-direction:column;align-items:center}
  .back-brand .brand-name{font-size:34px}
  .back-brand .brand-name small{font-size:34px}
  .back-url{position:absolute;left:0;right:0;top:828px;text-align:center;font-size:22px;letter-spacing:1.5px;color:var(--white)}
</style>
</head>
<body>

<section class="page cover">
  <div class="cover-backdrop" role="img" aria-label="Faded photo of a bright modern kitchen with recessed downlights"></div>
  <h1 class="cover-title"><span class="word">CATALOG</span><span class="years">2017-2018</span></h1>
  <div class="tile slate"></div>
  <div class="tile kitchen-wide" role="img" aria-label="Photo of a timber kitchen lit by ceiling downlights"></div>
  <div class="tile boardroom" role="img" aria-label="Photo of a boardroom with warm recessed lighting"></div>
  <div class="tile kitchen-small" role="img" aria-label="Photo of a kitchen and dining area with downlights"></div>
  <div class="tile brand">
    <span class="brand-mark"></span>
    <p class="brand-name">Brindlemoss<small>Electrical</small></p>
  </div>
  <p class="cover-url">www.brindlemoss.com.au</p>
</section>

<section class="page pricing">
  <h2 class="pricing-title">CHOOSE YOUR STYLE OF<br>LED DOWNLIGHTS</h2>
  <div class="product-table">
    <div class="table-head"><span class="col-photo"></span><span class="col-spec">Specification</span><span class="col-price">Price</span></div>
    <div class="table-row">
      <div class="col-photo"><div class="light-photo white" role="img" aria-label="Product photo of a white LED downlight"></div></div>
      <div class="col-spec"><p class="spec-name">Lorem ipsum dolor</p><ul class="spec-list"><li>Save 80% on your energy bills with LEDs</li><li>50,000 hours of life</li><li>Up to 7 years manufacturer's warranty</li><li>Brighter than halogen downlights</li></ul></div>
      <div class="col-price">000$</div>
    </div>
    <div class="table-row">
      <div class="col-photo"><div class="light-photo white" role="img" aria-label="Product photo of a white LED downlight with driver"></div></div>
      <div class="col-spec"><p class="spec-name">Lorem ipsum dolor</p><ul class="spec-list"><li>Save 80% on your energy bills with LEDs</li><li>50,000 hours of life</li><li>Up to 7 years manufacturer's warranty</li><li>Brighter than halogen downlights</li></ul></div>
      <div class="col-price">000$</div>
    </div>
    <div class="table-row">
      <div class="col-photo"><div class="light-photo black" role="img" aria-label="Product photo of a black LED downlight with driver"></div></div>
      <div class="col-spec"><p class="spec-name">Lorem ipsum dolor</p><ul class="spec-list"><li>Save 80% on your energy bills with LEDs</li><li>50,000 hours of life</li><li>Up to 7 years manufacturer's warranty</li><li>Brighter than halogen downlights</li></ul></div>
      <div class="col-price">000$</div>
    </div>
    <div class="table-row">
      <div class="col-photo"><div class="light-photo silver" role="img" aria-label="Product photo of a silver finned LED downlight"></div></div>
      <div class="col-spec"><p class="spec-name">Lorem ipsum dolor</p><ul class="spec-list"><li>Save 80% on your energy bills with LEDs</li><li>50,000 hours of life</li><li>Up to 7 years manufacturer's warranty</li><li>Brighter than halogen downlights</li></ul></div>
      <div class="col-price">000$</div>
    </div>
  </div>
  <div class="bulk-tab">Quarnil Sabeto 9w LED</div>
  <div class="bulk-panel">
    <p>1-10......lights : <b>$49</b></p>
    <p>21-40...lights : <b>$42</b></p>
    <p>11-20...lights : <b>$45</b></p>
    <p>40 and over : <b>$40</b></p>
  </div>
  <p class="pricing-url">www.brindlemoss.com.au</p>
</section>

<section class="page back">
  <div class="back-strip"></div>
  <div class="back-scene" role="img" aria-label="Teal-toned photo of a bedroom lit by ceiling downlights"></div>
  <div class="back-brand">
    <span class="brand-mark"></span>
    <p class="brand-name">Brindlemoss<small>Electrical</small></p>
  </div>
  <p class="back-url">www.brindlemoss.com.au</p>
</section>

</body>
</html>
```